1 page A4 double sided Brochure Design Folded to envelope size. Interesting fold design would be co

Small family run guesthouse BnB in Blue Mountains Australia needs a new brochure showing different aspects of business

We need a new brochure to go with our new website. Basically the design would be good as a double sided brochure that can be folded down to standard envelope size.

We have seen a few interesting brochure designs before that fold in different ways (and therefore have the design to match) but still fold down to this size to help with postage.

The design would have to showcase the different aspects of our business including individual accommodation for couples and families, conference market, wedding market, retreat market and events market (parties, re-unions etc). The Business must be Showcased as The Fernhollow Lodge, Blue Mountains

It is possible to arrange design so folds separate different sections of info/pictures.

It is also optional that we possibly have 2 brochures instead, one that is a basic all inclusive once described and one that only deals with group bookings (wedding conference retreats etc etc)

Must match design elements from our web page. Feel free to take informations, elements and images from there for design www.fernhollowlodge.com.au

Here is a link to our view we wake up to every morning to inspire all those working on a design!
http://www.fernhollowlodge.com.au/images/view.jpg

Target Market(s)

Group bookings, weddings, conferences, retreats, events and Blue Mountains Travellers

Industry/Entity Type

Accommodation

Requirements
Must have
• Must be based on our current websites design feel, colours, etc
Must be showcased as The Fernhollow Lodge Blue Mountains.
Must mention The Blue Mountains as a world heritage destination
Must be A4 double sided that can fold down to 1/3 the size to fit into a standard envelope. Any designs that will not fit in a standard envelope once folded can not be accepted as they are outside the brief
Nice to have
• Interesting folding design to get people interested to read it.

```html
<!DOCTYPE html>
<html lang="en">
<head>
<meta charset="utf-8">
<title>The Fernhollow Lodge – Brochure Back Page</title>
<link href="https://fonts.googleapis.com/css2?family=PT+Sans&family=Libre+Baskerville&display=swap" rel="stylesheet">
<style>
  :root {
    --stage: #c4c4c4;
    --band: #000000;
    --panel: #2a2a2a;
    --pattern: #1a1a1a;
    --text-light: #f2f2f2;
    --accent-red: #d4141b;
    --brand-bg: #35312c;
    --photo-sky: #b9c3c9;
    --photo-green: #5f7440;
    --photo-lawn: #7c9447;
  }
  html, body {
    margin: 0;
    width: 1200px;
    height: 750px;
    overflow: hidden;
    background: var(--stage);
    font-family: "PT Sans", Arial, sans-serif;
  }
  .brochure-page {
    position: absolute;
    left: 285px;
    top: 72px;
    width: 653px;
    height: 618px;
    background: var(--band);
    overflow: hidden;
  }
  .hero-photo {
    position: absolute;
    left: 0; top: 46px;
    width: 653px; height: 360px;
    background: linear-gradient(180deg, var(--photo-sky) 0%, #7d8a78 14%, var(--photo-green) 40%, #4f8f84 60%, var(--photo-lawn) 100%);
  }
  .lower-panel {
    position: absolute;
    left: 0; top: 0;
    width: 653px; height: 618px;
  }
  .pattern-strip {
    position: absolute;
    left: 0; top: 546px;
    width: 653px; height: 22px;
    background: var(--pattern);
  }
  .brand-box {
    position: absolute;
    left: 48px; top: 90px;
    width: 170px; height: 206px;
    background: var(--brand-bg);
    border: 2px solid #e8e8e8;
    box-sizing: border-box;
    display: flex;
    align-items: center;
    justify-content: center;
  }
  .brand-name {
    font-family: "Libre Baskerville", Georgia, serif;
    color: var(--text-light);
    font-size: 18px;
    line-height: 1.3;
    text-align: center;
    margin: 0;
  }
  .enquiries {
    position: absolute;
    left: 20px; top: 384px;
    width: 290px;
    text-align: center;
    color: var(--text-light);
    font-size: 9px;
    line-height: 12px;
  }
  .enquiries p { margin: 0; }
  .enquiries .contact {
    color: var(--accent-red);
    font-size: 12.5px;
    line-height: 14px;
  }
  .enquiries .phone { margin: 10px 0 14px; }
  .tagline {
    position: absolute;
    left: 395px; top: 357px;
    width: 230px;
    text-align: center;
    color: var(--accent-red);
    font-size: 13px;
    line-height: 31px;
  }
  .tagline p { margin: 0; }
  .closing-note {
    position: absolute;
    left: 262px; top: 490px;
    width: 390px;
    text-align: center;
    color: var(--text-light);
    font-size: 11.5px;
    line-height: 13px;
    text-transform: uppercase;
    margin: 0;
  }
</style>
</head>
<body>
  <main class="brochure-page">
    <div class="hero-photo" role="img" aria-label="Photo of the guesthouse pool terrace with lawn and umbrellas overlooking a forested Blue Mountains valley"></div>

    <svg class="lower-panel" width="653" height="618" viewBox="0 0 653 618" aria-hidden="true">
      <path fill="#2a2a2a" d="M0 378 C30 360 60 340 110 338 C170 336 230 352 280 375 C310 388 330 396 360 392 C400 386 430 330 480 305 C520 290 560 294 600 320 C625 336 640 345 653 350 L653 546 L0 546 Z"/>
    </svg>

    <div class="pattern-strip" role="img" aria-label="Decorative swirl pattern band"></div>

    <div class="brand-box">
      <p class="brand-name">The Fernhollow<br>Lodge</p>
    </div>

    <section class="enquiries">
      <p>For enquiries for either The Fernhollow Lodge or<br>Ridgeview Cottage you can call us any time at The Fernhollow Lodge on</p>
      <p class="contact phone">02 4700 1234</p>
      <p>Alternatively you can also email us for each property at<br>The Fernhollow Lodge</p>
      <p class="contact">info@fernhollowlodge.com.au</p>
      <p>Ridgeview Cottage</p>
      <p class="contact">info@ridgeviewcottage.com.au</p>
    </section>

    <section class="tagline">
      <p>Individual accommodation</p>
      <p>or Group stays</p>
      <p>So close by ... but worlds away</p>
    </section>

    <p class="closing-note">If you have any other questions while looking for your<br>Blue Mountains accommodation please contact us any time</p>
  </main>
</body>
</html>
```